Varnel Supply requires a new business card.

We are an online professional tool store.

Target Market(s)

We target the professional technician.

Industry/Entity Type

Business

Contact Information for Business Card

VarnelSupply.com.au

sales@varnelsupply.example

Requirements
Must have
• Needs to look commercial and professional
Should not have
• No Australian Colors, maps or shapes.
• No Shapes of Tools

```html
<!DOCTYPE html>
<html lang="en">
<head>
<meta charset="utf-8">
<title>Varnel Supply – Business Card</title>
<link href="https://fonts.googleapis.com/css2?family=Lato:wght@400;700&display=swap" rel="stylesheet">
<style>
  :root {
    --stage: #3b3b3d;
    --royal: #1024c4;
    --royal-deep: #0c1ca8;
    --cyan: #1296c8;
    --white: #ffffff;
  }
  * { box-sizing: border-box; margin: 0; padding: 0; }
  html, body { width: 1200px; height: 900px; overflow: hidden; }
  body {
    background: var(--stage);
    font-family: "Lato", Arial, sans-serif;
    display: flex;
    flex-direction: column;
    align-items: center;
    justify-content: center;
    gap: 60px;
  }
  .card {
    position: relative;
    width: 600px;
    height: 343px;
    border-radius: 4px;
    overflow: hidden;
    box-shadow: 0 14px 30px rgba(0,0,0,0.45);
  }

  /* Contact side */
  .card-contact { background: var(--white); }
  .contact-sweep { position: absolute; inset: 0; width: 600px; height: 343px; }
  .contact-details {
    position: absolute;
    left: 34px;
    top: 34px;
    color: var(--white);
    font-size: 14px;
    line-height: 1.45;
  }
  .person-name {
    color: var(--cyan);
    font-size: 26px;
    font-weight: 400;
    line-height: 1.1;
  }
  .person-role { font-size: 14px; margin-bottom: 14px; }
  .address { margin-bottom: 14px; }
  .contact-list { list-style: none; }
  .contact-list li { display: flex; align-items: center; gap: 8px; }
  .contact-list svg { width: 12px; height: 12px; fill: var(--cyan); flex: none; }
  .contact-list .no-icon { padding-left: 20px; }
  .contact-brand {
    position: absolute;
    left: 350px;
    right: 0;
    top: 120px;
    bottom: 0;
    display: flex;
    align-items: center;
    justify-content: center;
    gap: 12px;
  }

  /* Brand side */
  .card-brand {
    background: linear-gradient(135deg, var(--royal) 0%, var(--royal-deep) 100%);
    display: flex;
    flex-direction: column;
    align-items: center;
    justify-content: center;
    gap: 36px;
  }
  .brand-lockup { display: flex; align-items: center; gap: 14px; }
  .brand-dot { width: 22px; height: 22px; border-radius: 50%; background: var(--cyan); flex: none; }
  .brand-name {
    font-size: 40px;
    font-weight: 700;
    letter-spacing: 0.5px;
    white-space: nowrap;
  }
  .card-brand .brand-name { color: var(--white); }
  .card-contact .brand-name { color: var(--royal); font-size: 26px; }
  .card-contact .brand-dot { width: 18px; height: 18px; }
  .brand-web { color: var(--white); font-size: 16px; letter-spacing: 0.5px; }
</style>
</head>
<body>

  <section class="card card-contact" aria-label="Business card, contact side">
    <svg class="contact-sweep" viewBox="0 0 600 343" aria-hidden="true">
      <path d="M0 0 H430 C340 90 300 200 290 343 H0 Z" fill="var(--royal)"/>
      <path d="M430 0 H448 C358 90 318 200 308 343 H290 C300 200 340 90 430 0 Z" fill="var(--cyan)"/>
      <path d="M448 0 H456 C366 90 326 200 316 343 H308 C318 200 358 90 448 0 Z" fill="var(--royal)"/>
    </svg>

    <div class="contact-details">
      <h1 class="person-name">Dalen Ashcroft</h1>
      <p class="person-role">Manager</p>
      <p class="address">48 Corrin Street<br>Marlow, TX 75021</p>
      <ul class="contact-list">
        <li>
          <svg viewBox="0 0 24 24" aria-hidden="true"><path d="M6.6 10.8a15.1 15.1 0 0 0 6.6 6.6l2.2-2.2c.3-.3.7-.4 1-.2 1.1.4 2.3.6 3.6.6.6 0 1 .4 1 1V20c0 .6-.4 1-1 1A17 17 0 0 1 3 4c0-.6.4-1 1-1h3.5c.6 0 1 .4 1 1 0 1.3.2 2.5.6 3.6.1.3 0 .7-.2 1z"/></svg>
          555 014 2270
        </li>
        <li>
          <svg viewBox="0 0 24 24" aria-hidden="true"><path d="M6 3h10v5H6zM4 9h16a2 2 0 0 1 2 2v6h-4v4H6v-4H2v-6a2 2 0 0 1 2-2zm4 8v2h8v-4H8z"/></svg>
          555 014 2271
        </li>
        <li>
          <svg viewBox="0 0 24 24" aria-hidden="true"><path d="M2 5h20v14H2zm2 2v.5l8 5 8-5V7z"/></svg>
          sales@varnelsupply.example
        </li>
        <li class="no-icon">VarnelSupply.com.au</li>
      </ul>
    </div>

    <div class="contact-brand">
      <span class="brand-dot" aria-hidden="true"></span>
      <span class="brand-name">Varnel Supply</span>
    </div>
  </section>

  <section class="card card-brand" aria-label="Business card, brand side">
    <div class="brand-lockup">
      <span class="brand-dot" aria-hidden="true"></span>
      <span class="brand-name">Varnel Supply</span>
    </div>
    <p class="brand-web">www.VarnelSupply.com.au</p>
  </section>

</body>
</html>
```